Harvest of Kingdoms
preparing the way of the Lord...
Modern
Tom Farrel
412 Co.Rd. 118 Marlow, Pa.17602
tomjane4Faith@postvale.com
www.tf-harvestofkingdoms.com
preaching the gospel of Jesus, and teaching others to do the same.
mission trips
rallies and revivals
camps
this is for business cards and letterhead...

```html
<!DOCTYPE html>
<html lang="en">
<head>
<meta charset="utf-8">
<title>Harvest of Kingdoms — Business Card</title>
<link rel="stylesheet" href="https://fonts.googleapis.com/css2?family=Arimo:wght@400;700&display=swap">
<style>
  :root {
    --backdrop: #e9e6e1;
    --card: #ffffff;
    --ink: #2b2b2b;
    --ink-soft: #3d3d3d;
    --rule: #9a9a9a;
    --green-light: #8cc63f;
    --green-dark: #1f8f3a;
    --blue: #1f5fa6;
    --blue-light: #6fa5d8;
    --icon-green: #2e9a3a;
  }
  * { margin: 0; padding: 0; box-sizing: border-box; }
  html, body {
    width: 1200px;
    height: 804px;
    overflow: hidden;
    background: var(--backdrop);
    font-family: "Arimo", Arial, sans-serif;
  }
  .business-card {
    position: absolute;
    left: 50px;
    top: 142px;
    width: 1100px;
    height: 520px;
    background: var(--card);
    border-radius: 30px;
    overflow: hidden;
    box-shadow: 0 6px 18px rgba(0,0,0,0.18);
  }
  .card-wave {
    position: absolute;
    left: 0;
    bottom: 0;
    width: 1100px;
    height: 200px;
  }
  .brand {
    position: absolute;
    left: 100px;
    top: 212px;
    display: flex;
    align-items: center;
    gap: 12px;
  }
  .brand-dot {
    width: 30px;
    height: 30px;
    border-radius: 50%;
    background: var(--blue);
    flex: none;
  }
  .brand-name {
    font-size: 34px;
    font-weight: 700;
    color: var(--ink);
    white-space: nowrap;
    letter-spacing: 0.2px;
  }
  .divider {
    position: absolute;
    left: 543px;
    top: 94px;
    width: 2px;
    height: 262px;
    background: linear-gradient(to bottom, rgba(154,154,154,0), var(--rule) 20%, var(--rule) 80%, rgba(154,154,154,0));
  }
  .contact {
    position: absolute;
    left: 577px;
    top: 100px;
    color: var(--ink);
  }
  .contact-name {
    font-size: 31px;
    font-weight: 700;
    line-height: 1.1;
  }
  .contact-company {
    font-size: 21px;
    font-weight: 700;
    margin-top: 8px;
  }
  .contact-details {
    list-style: none;
    margin-top: 56px;
    font-size: 21px;
    color: var(--ink-soft);
    line-height: 34px;
  }
  .contact-details li {
    display: flex;
    align-items: center;
    gap: 10px;
  }
  .contact-details .icon {
    width: 18px;
    height: 18px;
    flex: none;
  }
</style>
</head>
<body>
  <main class="business-card">
    <div class="brand">
      <span class="brand-dot"></span>
      <span class="brand-name">Harvest of Kingdoms</span>
    </div>

    <div class="divider"></div>

    <section class="contact">
      <h1 class="contact-name">Tom Farrel</h1>
      <p class="contact-company">Harvest of Kingdoms</p>
      <ul class="contact-details">
        <li>412 Co.Rd. 118 Marlow, Pa.17602</li>
        <li>
          <svg class="icon" viewBox="0 0 20 20" aria-hidden="true">
            <path fill="var(--icon-green)" d="M5 2c1 0 2 3 2 4s-1 1.5-1 2c0 1 3 5 5 6 .6 0 1-1 2-1s4 1 4 2-1 3-3 3C8 18 2 11 2 6c0-2 2-4 3-4z"/>
          </svg>
          570.555.0192 (Toll Free)
        </li>
        <li>
          <svg class="icon" viewBox="0 0 20 20" aria-hidden="true">
            <rect x="1" y="4" width="18" height="12" rx="1.5" fill="var(--icon-green)"/>
            <path d="M2 5l8 6 8-6" fill="none" stroke="#fff" stroke-width="1.5"/>
          </svg>
          tomjane4Faith@postvale.com
        </li>
        <li>
          <svg class="icon" viewBox="0 0 20 20" aria-hidden="true">
            <circle cx="10" cy="10" r="9" fill="var(--icon-green)"/>
            <ellipse cx="10" cy="10" rx="4" ry="9" fill="none" stroke="#fff" stroke-width="1.2"/>
            <path d="M1 10h18" stroke="#fff" stroke-width="1.2"/>
          </svg>
          www.tf-harvestofkingdoms.com
        </li>
      </ul>
    </section>

    <svg class="card-wave" viewBox="0 0 1100 200" preserveAspectRatio="none" aria-hidden="true">
      <defs>
        <linearGradient id="greenBand" x1="0" y1="0" x2="0" y2="1">
          <stop offset="0" stop-color="var(--green-light)"/>
          <stop offset="1" stop-color="var(--green-dark)"/>
        </linearGradient>
        <linearGradient id="blueSwoosh" x1="0" y1="0" x2="1" y2="0">
          <stop offset="0" stop-color="var(--blue-light)"/>
          <stop offset="0.5" stop-color="var(--blue)"/>
          <stop offset="1" stop-color="var(--blue-light)"/>
        </linearGradient>
        <linearGradient id="greyHaze" x1="0" y1="0" x2="0" y2="1">
          <stop offset="0" stop-color="#ffffff" stop-opacity="0"/>
          <stop offset="1" stop-color="#d6d6d6"/>
        </linearGradient>
      </defs>
      <path d="M0 40 C 300 130, 650 150, 1100 20 L1100 120 L0 120 Z" fill="url(#greyHaze)"/>
      <path d="M0 62 C 280 150, 640 160, 1100 40 C 700 140, 300 140, 0 80 Z" fill="url(#blueSwoosh)"/>
      <path d="M0 55 C 300 140, 650 150, 1100 28" fill="none" stroke="#b9b9b9" stroke-width="2"/>
      <path d="M0 100 C 320 170, 700 160, 1100 62 L1100 200 L0 200 Z" fill="url(#greenBand)"/>
    </svg>
  </main>
</body>
</html>
```